New business card for civil engineering company - "Keystone Audit"

We need a business card designed for our new structural engineering company.

The company name is "Keystone Audit" logo files attached.

We would like the following:
* Two-sided card
* Simple design

Information to be placed on the card:
Name - Marcus Dellow
Job Title - Director / Structural Engineer
Credentials - BEng(Hons), CPEng, CMengNZ, IntPE(NZ)
Email - marcus.dellow@keystoneaudit.co.nz
mobile - 0219364058
website - www.keystoneaudit.co.nz

```html
<!DOCTYPE html>
<html lang="en">
<head>
<meta charset="utf-8">
<title>Keystone Audit — Business Card</title>
<link rel="stylesheet" href="https://fonts.googleapis.com/css2?family=Open+Sans:wght@400;600;800&display=swap">
<style>
  :root {
    --backdrop: #e6e7e9;
    --card-white: #ffffff;
    --navy: #14436f;
    --ink: #3a3a3c;
    --ink-soft: #7a7b7e;
    --brand-blue: #4a90d4;
    --accent-cyan: #29b6e8;
    --on-navy: #ffffff;
  }
  * { box-sizing: border-box; margin: 0; padding: 0; }
  html, body {
    width: 1200px; height: 977px; overflow: hidden;
    background: var(--backdrop);
    font-family: "Open Sans", Arial, sans-serif;
  }
  .sheet {
    width: 1200px; height: 977px;
    display: flex; flex-direction: column; align-items: center; justify-content: center;
    gap: 30px;
  }
  .card {
    width: 760px; height: 434px;
    position: relative;
    box-shadow: 0 6px 18px rgba(0,0,0,0.12);
  }
  /* Front */
  .card-front {
    background: var(--card-white);
    display: flex; flex-direction: column; align-items: center; justify-content: center;
  }
  .brand { display: flex; align-items: center; gap: 14px; }
  .brand-square { width: 26px; height: 26px; background: var(--brand-blue); }
  .brand-name {
    font-size: 42px; font-weight: 600; color: var(--ink);
    letter-spacing: 0.06em; text-transform: uppercase;
  }
  .brand-tagline {
    margin-top: 10px;
    font-size: 13px; font-weight: 400; color: var(--ink-soft);
    letter-spacing: 0.32em; text-transform: uppercase;
  }
  /* Back */
  .card-back { background: var(--navy); color: var(--on-navy); }
  .back-content { position: absolute; left: 80px; width: 610px; top: 118px; }
  .rule { height: 2px; background: var(--on-navy); }
  .rule-top { margin-left: 60px; }
  .holder-name {
    margin-top: 14px;
    font-size: 66px; font-weight: 800; line-height: 1;
    letter-spacing: -0.01em; text-transform: uppercase;
  }
  .holder-role {
    margin-top: 8px; margin-bottom: 14px;
    font-size: 13px; font-weight: 600; text-align: right;
  }
  .contact-row {
    margin-top: 14px;
    display: flex; gap: 16px; align-items: center;
    font-size: 14px; font-weight: 400;
  }
  .contact-item { display: flex; align-items: center; gap: 6px; white-space: nowrap; }
  .contact-icon { width: 13px; height: 13px; fill: var(--accent-cyan); flex: none; }
</style>
</head>
<body>
<main class="sheet">
  <section class="card card-front" aria-label="Card front">
    <div class="brand">
      <span class="brand-square"></span>
      <span class="brand-name">Keystone Audit</span>
    </div>
    <p class="brand-tagline">Peer Review Specialists</p>
  </section>

  <section class="card card-back" aria-label="Card back">
    <div class="back-content">
      <div class="rule rule-top"></div>
      <h1 class="holder-name">Marcus Dellow</h1>
      <p class="holder-role">Director / Structural Engineer, BEng(Hons), CPEng, CMengNZ, IntPE(NZ)</p>
      <div class="rule"></div>
      <div class="contact-row">
        <span class="contact-item">
          <svg class="contact-icon" viewBox="0 0 24 24" aria-hidden="true"><path d="M6.6 10.8a15.1 15.1 0 0 0 6.6 6.6l2.2-2.2a1 1 0 0 1 1-.25 11.4 11.4 0 0 0 3.6.57 1 1 0 0 1 1 1V20a1 1 0 0 1-1 1A17 17 0 0 1 3 4a1 1 0 0 1 1-1h3.5a1 1 0 0 1 1 1c0 1.25.2 2.45.57 3.57a1 1 0 0 1-.25 1z"/></svg>
          0219364058
        </span>
        <span class="contact-item">
          <svg class="contact-icon" viewBox="0 0 24 24" aria-hidden="true"><path d="M2 5h20v14H2z M2 5l10 8 10-8" fill-rule="evenodd"/><path d="M3 6l9 7 9-7v1.6l-9 7-9-7z" fill="#14436f"/></svg>
          marcus.dellow@keystoneaudit.co.nz
        </span>
        <span class="contact-item">
          <svg class="contact-icon" viewBox="0 0 24 24" aria-hidden="true"><circle cx="12" cy="12" r="10"/><circle cx="12" cy="12" r="4" fill="#14436f"/></svg>
          www.keystoneaudit.co.nz
        </span>
      </div>
    </div>
  </section>
</main>
</body>
</html>
```